Organic Herbs & Spices container

Greek startup company, which cultivate and trade spices and herbs (such as oregano, mint, thyme, sage etc.)

At present we are interested in only the type and shape of packaging which should be made by materials such as paper, cardboard, laminated paper and others based on paper or plastic.

Package size vary from 80g (2.82oz) - 300g (10.58oz). We are going to use the same packing for a variety of products with different information

* Please find attached our logo which should be included in the design.
* There is no company name available at the moment, however a name placeholder should be included.
* include a placeholder for the type of product (sage, oregano, mint, tea etc...).
* Each package should have a place in order to include product details and nutrition facts.

e.g.
xxxx (company name placeholder)
Sage (product type)
product details and nutrition facts.
Updates

Dear designers,first of all, thank you for your proposals. Please find bellow some updates for the project.- It is mandatory to include the logo into the design - Each package should be able to stored vertically - We are looking for one specific package design, please do not submit many variations of a certain package neither colour differentiations Thanks and good luck Added Wednesday, September 28, 2016

Please avoid the use of images. The same package will be used for all the kinds of products (only name and maybe colour will be different among different products. A transparent frame that will show the contents could be used too) Added Wednesday, September 28, 2016

Please find attached logo in EPS format

Our logo is the baseline, any concepts should be based on it. Try to avoid just adding the logo as a small sticker somewhere on the design. Please try to create around it at any way toy like. This could be, to visualize it as a 3D shape or object which can be used as the container of the products.

Reason: We would like to extend the time of the project. We believe that most of the submitted designs do not comply with our requirements.

Reason: We would like to see a bigger variety of ideas

Target Market(s)

Pretty much to anyone over 20 years old worldwide.

Industry/Entity Type

Nutrition

Requirements
Must have
• It should be attractive, easily recognized, simple yet innovative, durable, functional (easy to use) and easy to store.
Should not have
• Project must not include complex or obnoxious shapes and colours.

```html
<!DOCTYPE html>
<html lang="en">
<head>
<meta charset="utf-8">
<title>Organic Mint Container Label</title>
<link href="https://fonts.googleapis.com/css2?family=Montserrat:wght@500;700&family=Lobster&family=Amatic+SC:wght@700&family=Arimo:wght@400;700&display=swap" rel="stylesheet">
<style>
  :root {
    --page: #ffffff;
    --kraft: #c8ad80;
    --kraft-dark: #b89b6c;
    --green-dark: #3b6a1c;
    --green: #4f8a24;
    --green-light: #7fb23a;
    --band: #3f7a1a;
    --band-text: #e8dcb0;
    --ink: #3a3526;
    --frame: #5b6e3a;
  }
  * { box-sizing: border-box; margin: 0; padding: 0; }
  html, body { width: 1200px; height: 886px; overflow: hidden; background: var(--page); }
  .canvas { position: relative; width: 1200px; height: 886px; display: flex; justify-content: center; align-items: center; gap: 60px; }
  .label {
    position: relative; width: 340px; height: 780px;
    background: linear-gradient(180deg, var(--kraft) 0%, var(--kraft-dark) 100%);
    display: flex; flex-direction: column; align-items: center;
    color: var(--green-dark);
  }
  .organic {
    font-family: "Amatic SC", sans-serif; font-weight: 700; color: var(--green);
    letter-spacing: 1px; line-height: 1;
  }
  .product {
    font-family: "Lobster", cursive; font-weight: 400; color: var(--green-dark);
    line-height: 1; text-align: center;
  }
  .product-latin {
    display: block; font-size: 24px; color: var(--green);
    border-bottom: 1.5px solid var(--green); padding: 0 24px 2px; margin-top: -6px;
  }
  .company-frame {
    border: 1.5px solid var(--frame); outline: 1px solid var(--frame); outline-offset: 3px;
    padding: 14px 18px; font-family: "Montserrat", sans-serif; font-weight: 500;
    color: var(--ink); letter-spacing: 1.5px; font-size: 19px; text-align: center;
  }
  .company-frame b { font-weight: 700; }
  .brand {
    display: flex; flex-direction: column; align-items: center;
    font-family: "Montserrat", sans-serif; font-weight: 700; color: var(--green);
  }
  .brand-dot { border-radius: 50%; background: var(--green); }

  /* front */
  .front .organic { font-size: 34px; margin-top: 48px; }
  .front .product { font-size: 90px; margin-top: 6px; }
  .front .company-frame { margin-top: 28px; }
  .front .brand { font-size: 34px; gap: 18px; margin-top: 42px; }
  .front .brand-dot { width: 230px; height: 230px; }
  .weight-band {
    position: absolute; left: 0; right: 0; bottom: 28px; height: 32px;
    background: var(--band); color: var(--band-text);
    font-family: "Montserrat", sans-serif; font-weight: 700; font-size: 14px; letter-spacing: 1px;
    display: flex; align-items: center; justify-content: center;
  }

  /* back */
  .back .brand { font-size: 20px; gap: 8px; margin-top: 34px; }
  .back .brand-dot { width: 80px; height: 80px; }
  .back .company-frame { margin-top: 22px; }
  .back .product { font-size: 84px; margin-top: 18px; }
  .back .organic { font-size: 46px; margin-top: 10px; }
  .nutrition {
    width: 250px; margin-top: 14px; border: 1px solid var(--ink); padding: 6px 8px;
    font-family: "Arimo", sans-serif; color: #1e1c16; font-size: 8px; line-height: 1.3;
  }
  .nutrition h3 { font-size: 22px; font-weight: 700; line-height: 1.1; }
  .nutrition .rule-thick { height: 7px; background: #1e1c16; margin: 3px 0; }
  .nutrition .rule-mid { height: 3px; background: #1e1c16; margin: 3px 0; }
  .nutrition .row { display: flex; justify-content: space-between; }
  .nutrition .indent { padding-left: 12px; }
  .nutrition strong { font-weight: 700; }
  .nutrition .note { margin-top: 3px; font-size: 7px; }
</style>
</head>
<body>
<main class="canvas">

  <section class="label front" aria-label="Front of label">
    <p class="organic">Organic</p>
    <h1 class="product">Mint<span class="product-latin">Mentha</span></h1>
    <div class="company-frame"><b>COMPANY</b> NAME</div>
    <div class="brand"><span class="brand-dot"></span>Aetheria</div>
    <div class="weight-band">80 GM (2.82 OZ)</div>
  </section>

  <section class="label back" aria-label="Back of label">
    <div class="brand"><span class="brand-dot"></span>Aetheria</div>
    <div class="company-frame"><b>COMPANY</b> NAME</div>
    <h2 class="product">Mint<span class="product-latin">Mentha</span></h2>
    <p class="organic">Organic</p>
    <div class="nutrition">
      <h3>Nutrition Facts</h3>
      <div><strong>Serving Size 11g</strong></div>
      <div><strong>Servings per Container 4</strong></div>
      <div class="rule-thick"></div>
      <div>Amount Per Serving</div>
      <div class="row"><span>Calories 25</span><span>Calories from Fat 0</span></div>
      <div class="rule-mid"></div>
      <div class="row"><span></span><strong>% Daily Values*</strong></div>
      <div class="row"><span><strong>Total Fat</strong> 0g</span><span>0%</span></div>
      <div class="row indent"><span>Saturated Fat 0g</span><span>0%</span></div>
      <div class="row indent"><span>Trans Fat 0g</span><span>0%</span></div>
      <div class="row"><span><strong>Cholesterol</strong> 15mg</span><span>5%</span></div>
      <div class="row"><span><strong>Sodium</strong> 1025mg</span><span>43%</span></div>
      <div class="row"><span><strong>Total Carbohydrate</strong> 5g</span><span>1%</span></div>
      <div class="row indent"><span>Dietary Fiber 1g</span><span>4%</span></div>
      <div class="row indent"><span>Sugars 1g</span><span></span></div>
      <div class="row"><span><strong>Protein</strong> 3g</span><span></span></div>
      <div class="rule-thick"></div>
      <p class="note">*Percent Daily Values are based on a 2,000 calorie diet. Your Daily Values may be higher or lower depending on your calorie needs.</p>
    </div>
  </section>

</main>
</body>
</html>
```